Travel Consultant Business Card

Hello.. New travel consultant looking seeking a business card that incorporates my new logo. I specialize in cruises but also want to imply land vacation. I am very open to any design and font concepts. I'm looking for a very upbeat modern design that reflects cruise and land vacations. Bright vibrant colors

Target Market(s)

Cruise and Land Vacationers

Industry/Entity Type

Travel Agent

Contact Information for Business Card

I am very open to any design and font concepts. I'm looking for a very upbeat modern design that reflects cruise and land vacations. Bright vibrant colors

Colors

Designer to choose colors to be used in the design.

Requirements
Must have
• Company Name: PineRidge Journeys---New logo uploaded to be included in design
• My Name: Danielle Marchetti-Travel Consultant
• Phone Number: (555) 418-7093
• E-Mail Address: pineridgejourneys@mailbox-example.com
• Website: www.pineridgejourneys-example.com
Nice to have
• My tag line is …..Guiding Every Journey

```html
<!DOCTYPE html>
<html lang="en">
<head>
<meta charset="UTF-8">
<title>PineRidge Journeys – Business Card</title>
<link rel="stylesheet" href="https://fonts.googleapis.com/css2?family=Open+Sans:wght@400;600&family=Raleway:wght@700;800&display=swap">
<style>
  :root {
    --navy: #1d5aab;
    --navy-deep: #1a4f98;
    --sky: #29a7e1;
    --ink: #111111;
    --paper: #ffffff;
    --backdrop: #eef1f4;
    --shadow: rgba(20, 40, 70, 0.22);
  }
  * { box-sizing: border-box; margin: 0; padding: 0; }
  html, body { width: 833px; height: 1200px; overflow: hidden; }
  body {
    background: var(--backdrop);
    font-family: "Open Sans", Arial, sans-serif;
    display: flex;
    flex-direction: column;
    align-items: center;
    justify-content: center;
    gap: 90px;
  }
  .card {
    position: relative;
    width: 640px;
    height: 366px;
    background: var(--paper);
    box-shadow: 0 10px 26px var(--shadow);
    overflow: hidden;
  }

  /* Front */
  .card--front::before,
  .card--front::after {
    content: "";
    position: absolute;
    left: 0; right: 0;
    height: 10px;
  }
  .card--front::before { top: 0; background: var(--navy); }
  .card--front::after { bottom: 0; background: var(--sky); }
  .wordmark {
    display: flex;
    align-items: center;
    gap: 12px;
    font-family: "Raleway", Arial, sans-serif;
    font-weight: 800;
    color: var(--navy);
    white-space: nowrap;
  }
  .wordmark__dot {
    border-radius: 50%;
    background: var(--sky);
    flex: none;
  }
  .card--front .wordmark {
    position: absolute;
    top: 50%; left: 50%;
    transform: translate(-50%, -50%);
    font-size: 44px;
  }
  .card--front .wordmark__dot { width: 20px; height: 20px; }

  /* Back */
  .back-shapes { position: absolute; inset: 0; }
  .identity {
    position: absolute;
    left: 42px;
    top: 56px;
  }
  .identity .wordmark { font-size: 28px; gap: 8px; }
  .identity .wordmark__dot { width: 13px; height: 13px; }
  .tagline {
    margin-top: 14px;
    font-size: 17px;
    letter-spacing: 0.5px;
    color: var(--ink);
  }
  .person__name {
    margin-top: 18px;
    font-family: "Raleway", Arial, sans-serif;
    font-weight: 800;
    font-size: 25px;
    color: var(--sky);
  }
  .person__title {
    font-family: "Raleway", Arial, sans-serif;
    font-weight: 700;
    font-size: 17px;
    color: var(--ink);
  }
  .contacts {
    position: absolute;
    right: 34px;
    top: 190px;
    list-style: none;
  }
  .contacts::after {
    content: "";
    position: absolute;
    right: 12px;
    top: 14px;
    bottom: 14px;
    width: 2px;
    background: var(--sky);
  }
  .contacts__item {
    display: flex;
    align-items: center;
    justify-content: flex-end;
    gap: 14px;
    height: 26px;
    margin-bottom: 17px;
    font-size: 17px;
    color: var(--paper);
  }
  .contacts__icon {
    position: relative;
    z-index: 1;
    width: 26px;
    height: 26px;
    border-radius: 50%;
    background: var(--sky);
    display: flex;
    align-items: center;
    justify-content: center;
    flex: none;
  }
  .contacts__icon svg { width: 14px; height: 14px; }
</style>
</head>
<body>

  <section class="card card--front" aria-label="Business card front">
    <div class="wordmark"><span class="wordmark__dot"></span>PineRidge Journeys</div>
  </section>

  <section class="card card--back" aria-label="Business card back">
    <svg class="back-shapes" viewBox="0 0 640 366" preserveAspectRatio="none" aria-hidden="true">
      <polygon points="0,366 540,0 640,0 640,366" fill="var(--navy)"/>
      <polygon points="505,40 640,0 640,250" fill="var(--sky)"/>
      <polygon points="505,40 600,40 640,250" fill="var(--navy-deep)"/>
    </svg>

    <div class="identity">
      <div class="wordmark"><span class="wordmark__dot"></span>PineRidge Journeys</div>
      <p class="tagline">Guiding Every Journey</p>
      <p class="person__name">Danielle Marchetti</p>
      <p class="person__title">Travel Consultant</p>
    </div>

    <ul class="contacts">
      <li class="contacts__item">(555) 418-7093
        <span class="contacts__icon">
          <svg viewBox="0 0 24 24"><path fill="#fff" d="M6.6 10.8a15.1 15.1 0 0 0 6.6 6.6l2.2-2.2c.3-.3.7-.4 1-.2 1.1.4 2.3.6 3.6.6.6 0 1 .4 1 1V20c0 .6-.4 1-1 1A17 17 0 0 1 3 4c0-.6.4-1 1-1h3.5c.6 0 1 .4 1 1 0 1.3.2 2.5.6 3.6.1.3 0 .7-.2 1z"/></svg>
        </span>
      </li>
      <li class="contacts__item">pineridgejourneys@mailbox-example.com
        <span class="contacts__icon">
          <svg viewBox="0 0 24 24"><rect x="3" y="6" width="18" height="12" rx="1" fill="none" stroke="#fff" stroke-width="2"/><path d="M3 7l9 6 9-6" fill="none" stroke="#fff" stroke-width="2"/></svg>
        </span>
      </li>
      <li class="contacts__item">www.pineridgejourneys-example.com
        <span class="contacts__icon">
          <svg viewBox="0 0 24 24" fill="none" stroke="#fff" stroke-width="2"><circle cx="12" cy="12" r="9"/><ellipse cx="12" cy="12" rx="4" ry="9"/><path d="M3 12h18"/></svg>
        </span>
      </li>
    </ul>
  </section>

</body>
</html>
```